Short-Term Rental Website - Management Services for Property Owner

We are looking for a website to advertise our short-term rental business, Bright Door Stay Management, currently www.brightdoor.ca. Hosted on WordPress.

We have the website main page language but we are looking for someone who is creative and can present the information in a trendy, cool and professional way. I like the closed design crowd job "Plumfield Marketing - SEM, Influencer website. FUN RETRO VIBES" (see attached pictures) in terms of how the page flows, icons and stock images, other connective imagery and design features

Our main competitor website is www.stayvora.com and we like how that website feels but we like the elegance of www.Halvorn-Trask.com (desktop) and main page of www.pombridge.ca (desktop version). We like the slow type video on pombridge.com.

MUST LOOK GOOD ON MOBILE. The mobile experience has to be good.

The content in terms of the language is in one of the attached files.

Our landing page requires the following sections;
- Revenue Maximization
- Services (I have included the content that we want highlighted but we are looking for someone to be creative with how these are displayed
- Pricing
- Featured Properties (display on a carousel) *must design a carousel that can be easily populated.
- Reviews (display on a carousel) *must design a carousel that can be easily populated.
- Contact Us (first name, last name, email, phone (required), description of property)

The header will have;
- Logo (link to main page)
- Pricing (link to pricing section found on the main page)
- Services (link to services section found on the main page)
- Properties (separate page)
- Contact (link to contact area on main page)

We would also need a coded template page that we could use to add additional pages as needed.

For the properties page, we need a landing page that would allow our guests to see all of our properties and a map view with the properties plotted on the map.

As we would collect personal information we would need a cookies/ privacy policy.

The colour palette should be on the light side. We do not want the website to have a dark feel. Colours should be consistent with that of our logo but we are open to creativity.

Target Market(s)

Investment property owners

Industry/Entity Type

Real Estate

Coding

Coded - Design and coding required

Number of Pages Required

2 page

Font styles to use
Sans Serif

Requirements
Must have
• Very strong and well designed landing page

Second page which showcases properttes

Template property page that can be easily reproduced

```html
<!DOCTYPE html>
<html lang="en">
<head>
<meta charset="utf-8">
<title>Bright Door Stay Management – Services</title>
<link href="https://fonts.googleapis.com/css2?family=Montserrat:ital,wght@0,500;0,600;0,700;1,600;1,700&family=Questrial&display=swap" rel="stylesheet">
<style>
  :root {
    --page-bg: #ffffff;
    --band-teal: #4f7f8a;
    --band-text: #ffffff;
    --heading-dark: #4a4a4a;
    --title-grey: #555555;
    --body-grey: #6a6a6a;
    --accent-blue: #1f5fae;
    --accent-mint: #6de0a0;
    --pricing-bg: #f2f2f2;
  }
  * { margin: 0; padding: 0; box-sizing: border-box; }
  html, body { width: 1200px; height: 1200px; overflow: hidden; background: var(--page-bg); }
  body { position: relative; font-family: "Questrial", sans-serif; }

  .intro-band {
    position: absolute; left: 101px; top: 101px; width: 1006px; height: 306px;
    background: var(--band-teal); color: var(--band-text);
    font-family: "Montserrat", sans-serif;
  }
  .intro-col { position: absolute; }
  .intro-col h2 {
    font-style: italic; font-weight: 600; font-size: 17px; line-height: 21.5px;
    margin-bottom: 14px; letter-spacing: 0.1px;
  }
  .intro-col p { font-weight: 500; font-size: 10.6px; line-height: 14.4px; margin-bottom: 17px; }
  .intro-about { left: 97px; top: 21px; width: 262px; }
  .intro-about p { letter-spacing: 0.35px; }
  .intro-str { left: 375px; top: 20px; width: 268px; }
  .intro-fee { left: 660px; top: 21px; width: 256px; }

  .section-title {
    position: absolute; left: 0; width: 1200px; text-align: center;
    font-family: "Montserrat", sans-serif; font-weight: 700; font-size: 34px;
    color: var(--heading-dark); letter-spacing: -0.3px;
  }
  .section-rule { position: absolute; height: 2px; width: 37px; }
  .services-title { top: 445px; left: -9px; }
  .services-rule { left: 576px; top: 488px; background: var(--accent-blue); }

  .service { position: absolute; top: 540px; }
  .service-icon { position: absolute; width: 92px; height: 92px; border-radius: 10px;
    background: linear-gradient(160deg, #e9f3f8 0%, #bfe9da 55%, #5cc9a7 100%); }
  .service-name {
    position: absolute; top: 109px; white-space: nowrap; transform: translateX(-50%);
    font-size: 16.5px; color: var(--title-grey); letter-spacing: 0.2px;
  }
  .service-rule { position: absolute; top: 139px; height: 2px; width: 37px;
    background: var(--accent-blue); transform: translateX(-50%); }
  .service-list { position: absolute; top: 158px; list-style: none; width: 190px; }
  .service-list li {
    position: relative; padding-left: 9px; font-size: 11.3px; line-height: 14.4px;
    color: var(--body-grey); margin-bottom: 12.6px;
  }
  .service-list li::before {
    content: ""; position: absolute; left: 0; top: 5px; width: 4px; height: 4px;
    border-radius: 50%; background: var(--accent-blue);
  }
  .list-tight li { margin-bottom: 5px; }
  .list-tight li:first-child { margin-bottom: 12.6px; }
  .footnote { position: absolute; font-size: 8.4px; line-height: 11px; color: var(--body-grey);
    letter-spacing: 0.4px; width: 200px; }

  .pricing-band {
    position: absolute; left: 101px; top: 993px; width: 1006px; height: 114px;
    background: var(--pricing-bg);
  }
  .pricing-title { top: 1036px; left: 9px; }
  .pricing-rule { left: 592px; top: 1082px; background: var(--accent-mint); }
</style>
</head>
<body>

<section class="intro-band">
  <div class="intro-col intro-about">
    <h2>At Bright Door Stay Management, we manage the entire hosting process, so you don't have to.</h2>
    <p>We do much more than provide a hassle-free experience, we specialize in maximizing the revenue from your property.</p>
    <p>As a Short-Term Rental (STR), your property is able to take advantage of peak rental demand periods which results in significantly greater revenue than a traditional rental property.</p>
  </div>
  <div class="intro-col intro-str">
    <h2>What is a Short-Term Rental (STR)?</h2>
    <p>A Short-Term Rental (STR) is a property that is typically rented for duration of less than 30-days. Although the property is rented for shorter durations (on average between 3-7 days), we would manage the property year-round.</p>
    <p>By renting on a shorter term, you are able to take advantage of peak demand periods throughout the year (Stampede, etc.) which results in a much higher revenue potential. With a significant amount of long-term rental inventory in Calgary, short-term rentals provide a solution to home owners and investor.</p>
  </div>
  <div class="intro-col intro-fee">
    <h2>How is the management fee calculated?</h2>
    <p>We strive to keep our fee as simple as possible with 80% of revenue going to you, 20% to Bright Door for the management and the cleaning fee is paid for by the guest.</p>
    <p>For more information on our service options, please see our pricing area.</p>
  </div>
</section>

<h2 class="section-title services-title">SERVICES</h2>
<div class="section-rule services-rule"></div>

<div class="service" style="left:0">
  <div class="service-icon" role="img" aria-label="Icon of a host holding out a hand to a guest" style="left:254px;top:0"></div>
  <h3 class="service-name" style="left:299px">Guest Experience</h3>
  <div class="service-rule" style="left:286px"></div>
  <ul class="service-list" style="left:184px">
    <li>End-to-end management of the guest experience</li>
    <li>Local Calgary Experts (events, guidebook, advice)</li>
    <li>Rapid response time to guest messages</li>
    <li>24/7 Guest Support</li>
    <li>On-Site Services (check-in, maintenance, etc.)</li>
    <li>Professional Photography</li>
    <li>Tablet for Guest Use</li>
  </ul>
</div>

<div class="service" style="left:0">
  <div class="service-icon" role="img" aria-label="Icon of a padlock with a cross mark" style="left:466px;top:0"></div>
  <h3 class="service-name" style="left:512px">Safety &amp; Security</h3>
  <div class="service-rule" style="left:513px"></div>
  <ul class="service-list" style="left:392px">
    <li>Smart Lock (Condo Compliant)</li>
    <li>Sensory Security Devices (non-invasive, real-time data)</li>
    <li>Insurance for damage provided by Stayhaven*</li>
    <li>Enhanced Guest Screening</li>
    <li>Ongoing Guest Risk Assessment</li>
  </ul>
  <p class="footnote" style="left:386px;top:324px">* we recommend all homeowners purchase additional insurance as desired</p>
</div>

<div class="service" style="left:0">
  <div class="service-icon" role="img" aria-label="Icon of a house being cleaned" style="left:657px;top:0"></div>
  <h3 class="service-name" style="left:702px">Home Care</h3>
  <div class="service-rule" style="left:701px"></div>
  <ul class="service-list" style="left:608px">
    <li>Professional cleaning with unique cleaning guide</li>
    <li>Staging guide created for consistent appearance</li>
    <li>Inventory and replenishment of essentials</li>
    <li>Property inspection between reservations</li>
    <li>Linen service including towels</li>
    <li>Coordination of maintenance</li>
  </ul>
</div>

<div class="service" style="left:0">
  <div class="service-icon" role="img" aria-label="Icon of a rising bar chart with an arrow" style="left:873px;top:0"></div>
  <h3 class="service-name" style="left:924px">Performance Optimization</h3>
  <div class="service-rule" style="left:911px"></div>
  <ul class="service-list list-tight" style="left:822px">
    <li>Proprietary Pricing Tool used Only by Bright Door</li>
    <li>Strategic Calendar Management</li>
    <li>#1 &amp; #5 Highest Revenue 2-Bedroom Listings in Calgary</li>
    <li>Enhanced Analytics (above what Stayhaven provides)</li>
    <li>Monthly Property Performance Review</li>
  </ul>
</div>

<section class="pricing-band"></section>
<h2 class="section-title pricing-title">PRICING</h2>
<div class="section-rule pricing-rule"></div>

</body>
</html>
```